Invitation reopening cosmetics studio

On April 28, we will start the reopening of the cosmetically studio and brew a flyer. In the supplement: - two pictures of mine - my idea of ​​flyer presentation - various logos - brochures as thought aid - 20% to the reopening -28.04.2018 from 10.00 - 20.00 o'clock - Studio is small but charming On April 28 we will reopen the opening of the cosmetically studio start and brew a flyer. In the supplement: - two pictures of mine - my idea of ​​flyer presentation - various logos - brochures as thought aid - 20% to the reopening -28.04.2018 from 10.00 - 20.00 o'clock - Studio is small but charming On April 28 we will reopen the opening of the cosmetically studio start and brew a flyer. In the supplement: - two pictures of mine - my idea of ​​flyer presentation - various logos - brochures as thought aid - 20% for reopening - 28.04.2018 from 10.00 - 20.00 o'clock - Studio is small but charming on 28. April we will start the reopening of the cosmetically studio and brew a flyer. In the supplement: - two pictures of mine - my idea of ​​flyer presentation - various logos - brochures as thought aid - 20% to the reopening -28.04.2018 from 10.00 - 20.00 o'clock - Studio is small but charming On April 28 we will reopen the opening of the cosmetically studio start and brew a flyer. In the supplement: - two pictures of mine - my idea of ​​flyer presentation - various logos - brochures as thought aid - 20% to the reopening -28.04.2018 from 10.00 - 20.00 o'clock - Studio is small but charming On April 28 we will reopen the opening of the cosmetically studio start and brew a flyer. In the supplement: - two pictures of mine - my idea of ​​flyer presentation - various logos - brochures as thought aid - 20% for reopening - 28.04.2018 from 10.00 - 20.00 o'clock - Studio is small but charming on 28. April we will start the reopening of the cosmetically studio and brew a flyer. In the supplement: - two pictures of mine - my idea of ​​flyer presentation - various logos - brochures as thought aid - 20% to the reopening -28.04.2018 from 10.00 - 20.00 o'clock - Studio is small but charming On April 28 we will reopen the opening of the cosmetically studio start and brew a flyer. In the supplement: - two pictures of mine - my idea of ​​flyer presentation - various logos - brochures as thought aid - 20% for reopening - 28.04.2018 from 10.00 - 20.00 o'clock - Studio is small but charming Medical cosmetics facials with high quality products Velmorine body treatments Depilation Pedicure Manicure Skin Analysis Medical Cosmetics Facials with high quality products Velmorine Body Treatments Depilation

Target Market(s)

Medical Cosmetics Facials with high quality products Velmorine Body Treatments Depilation Pedicure Manicure Skin Analysis Medical Cosmetics Facials with high quality products Velmorine Body Treatments Depilation

Industry/Entity Type

Cosmetic

Font styles to use
Sans Serif

Colors
fece3e
fee18a

Requirements
Must have
• The key data simple and simple, elegant, charming,
Nice to have
• Picture of me, when, where, personal, location, picture of me, when, where, personal, location, picture of me, when, where, personal, location, picture of me, when, where, personal, location, picture of me, when, where, personal, location, picture of me, when, where, personal, location,
Should not have
• different color, too full, different color, too full, different color, too full, different color, too full, different color, too full, different color, too full, different color, too full, different color, too full, different color , too full, different color, too full, different color, too full, different color, too full, different color, too full, different color, too full, different color, too full, different color, too full, different color, too full v

```html
<!DOCTYPE html>
<html lang="de">
<head>
<meta charset="utf-8">
<title>Lumara Skin Studio – Eröffnungs-Apéro</title>
<link rel="stylesheet" href="https://fonts.googleapis.com/css2?family=Roboto:wght@400;500;700&display=swap">
<style>
  :root {
    --gold: #c9a233;
    --gold-light: #fee18a;
    --gold-bright: #fece3e;
    --gold-deep: #a8842a;
    --gold-text: #e3c256;
    --ink: #141414;
    --paper: #ffffff;
  }
  * { box-sizing: border-box; margin: 0; padding: 0; }
  html, body { width: 960px; height: 1200px; overflow: hidden; background: var(--paper); }
  body { font-family: "Roboto", Arial, sans-serif; color: var(--ink); }
  .flyer { position: relative; width: 960px; height: 1200px; background: var(--paper); overflow: hidden; }
  .artwork { position: absolute; left: 0; top: 0; width: 960px; height: 800px; }

  .brand { position: absolute; left: 36px; top: 46px; display: flex; align-items: center; gap: 12px; }
  .brand-dot { width: 52px; height: 52px; border-radius: 50%; border: 3px solid var(--gold); }
  .brand-name { font-size: 25px; font-weight: 500; color: var(--gold); letter-spacing: .3px; }

  .service { position: absolute; border-radius: 50%; background: var(--paper); border: 4px solid var(--gold);
    display: flex; flex-direction: column; align-items: center; justify-content: center;
    font-weight: 500; font-size: 17px; line-height: 28px; text-align: center; }
  .service--face { left: 694px; top: 324px; width: 236px; height: 236px; }
  .service--body { left: 395px; top: 470px; width: 204px; height: 204px; }
  .service--hands { left: 122px; top: 580px; width: 168px; height: 168px; }

  .headline { position: absolute; right: 80px; top: 610px; text-align: right; color: var(--gold-text);
    font-size: 19px; line-height: 43px; }
  .headline strong { font-weight: 700; }

  .quote { position: absolute; left: 60px; width: 840px; top: 810px; text-align: center;
    font-size: 19px; font-weight: 500; line-height: 36px; text-transform: uppercase; }
  .quote-heart { display: inline-block; width: 18px; height: 16px; vertical-align: -1px; margin: 0 2px 0 10px; }
  .quote-mark { position: absolute; font-size: 64px; font-weight: 700; font-style: italic; color: var(--gold); line-height: 1; }
  .quote-mark--open { left: 34px; top: 796px; }
  .quote-mark--close { left: 900px; top: 896px; }

  .details { position: absolute; left: 51px; top: 948px; width: 808px; height: 182px;
    border: 2px solid var(--gold); border-radius: 40px; text-align: center; padding-top: 22px;
    font-size: 18px; line-height: 29px; }
  .details-title { color: var(--gold-text); font-size: 18px; }
  .details-time { font-size: 26px; font-weight: 700; }

  .footer { position: absolute; left: 0; top: 1148px; width: 960px; height: 52px;
    background: linear-gradient(90deg, var(--gold-deep), var(--gold-bright) 45%, var(--gold) 70%, var(--gold-deep));
    display: flex; align-items: center; justify-content: space-between; padding: 0 28px;
    color: var(--paper); font-size: 14px; font-weight: 500; }
  .footer-item { display: flex; align-items: center; gap: 8px; }
  .footer-item svg { width: 16px; height: 16px; }
</style>
</head>
<body>
<main class="flyer">
  <svg class="artwork" viewBox="0 0 960 800">
    <defs>
      <radialGradient id="photoTone" cx="540" cy="330" r="560" gradientUnits="userSpaceOnUse">
        <stop offset="0" stop-color="#c9a594"/>
        <stop offset=".22" stop-color="#8a6a5c"/>
        <stop offset=".45" stop-color="#3a2f2b"/>
        <stop offset=".7" stop-color="#56604c"/>
        <stop offset="1" stop-color="#7c8570"/>
      </radialGradient>
      <linearGradient id="goldBand" x1="0" y1="1" x2="1" y2="0">
        <stop offset="0" stop-color="#a8842a"/>
        <stop offset=".5" stop-color="#fece3e"/>
        <stop offset="1" stop-color="#b8922c"/>
      </linearGradient>
    </defs>
    <path role="img" aria-label="Portrait photo of the studio owner with dark wavy hair, outdoors with soft green foliage"
      d="M458,0 L960,0 L960,150 C880,330 760,420 620,470 C440,530 120,580 0,773 L0,297 C120,180 380,160 458,0 Z"
      fill="url(#photoTone)"/>
    <path d="M0,297 C120,180 380,160 458,0" fill="none" stroke="url(#goldBand)" stroke-width="10"/>
    <path d="M960,150 C880,330 760,420 620,470 C440,530 120,580 0,773" fill="none" stroke="url(#goldBand)" stroke-width="16"/>
  </svg>

  <div class="brand">
    <span class="brand-dot"></span>
    <span class="brand-name">Lumara Skin Studio</span>
  </div>

  <div class="service service--face">
    <span>Velmorine</span><span>Hautanalyse</span><span>Gesichtsbehandlungen</span><span>Medizinische Kosmetik</span>
  </div>
  <div class="service service--body">
    <span>Epilation</span><span>Sugaring</span><span>Bodybehandlungen</span>
  </div>
  <div class="service service--hands">
    <span>Pedicure</span><span>Manicure</span>
  </div>

  <div class="headline">
    <div>PERSÖNLICHE</div>
    <div>EINLADUNG</div>
    <div>ERÖFFNUNGS-APÉRO</div>
    <div><strong>LUMARA SKIN STUDIO</strong></div>
  </div>

  <span class="quote-mark quote-mark--open">“</span>
  <p class="quote">Es sind alle<svg class="quote-heart" viewBox="0 0 20 18"><path d="M10,17 C4,12 0,9 0,5 C0,2 2,0 5,0 C7,0 9,1 10,3 C11,1 13,0 15,0 C18,0 20,2 20,5 C20,9 16,12 10,17 Z" fill="var(--gold-text)"/></svg>-lich eingeladen, kommt vorbei und lernt das kleine<br>aber sehr charmante Kosmetikstudio kennen. Zusätzlich findet<br>ein kleines Apero für alle statt.</p>
  <span class="quote-mark quote-mark--close">”</span>

  <section class="details">
    <div class="details-title">ICH FREUE MICH BEREITS AUF EUCH</div>
    <div>Eröffnungs-Apéro</div>
    <div>Wann: 28 April 2018 &nbsp;von <span class="details-time">10–20 Uhr</span></div>
    <div>Wo: Lindenplatz 5, CH-8700 Seedorf</div>
    <div>Eröffnungsrabatt: 20% auf alle Produkte</div>
  </section>

  <footer class="footer">
    <span class="footer-item"><svg viewBox="0 0 16 16"><path d="M8,0 C4.7,0 2,2.6 2,5.8 C2,10 8,16 8,16 C8,16 14,10 14,5.8 C14,2.6 11.3,0 8,0 Z M8,8.2 A2.4,2.4 0 1 1 8,3.4 A2.4,2.4 0 1 1 8,8.2 Z" fill="#fff"/></svg>Lindenplatz 5, CH-8700 Seedorf</span>
    <span class="footer-item"><svg viewBox="0 0 16 16"><path d="M1,9 C1,5 15,5 15,9 L15,11 L11,11 L11,9 C9,8.4 7,8.4 5,9 L5,11 L1,11 Z" fill="#fff"/></svg>+41 79 000 12 34</span>
    <span class="footer-item"><svg viewBox="0 0 16 16"><rect x="1" y="3" width="14" height="10" fill="#fff"/><path d="M1,3 L8,9 L15,3" fill="none" stroke="#c9a233" stroke-width="1.4"/></svg>kontakt@lumara-skin.ch</span>
    <span class="footer-item"><svg viewBox="0 0 16 16"><g fill="none" stroke="#fff" stroke-width="1.3"><circle cx="8" cy="8" r="7"/><ellipse cx="8" cy="8" rx="3" ry="7"/><path d="M1,8 H15 M2.5,4.5 H13.5 M2.5,11.5 H13.5"/></g></svg>www.lumara-skin.ch</span>
  </footer>
</main>
</body>
</html>
```